Banner Ads for Zelvoranet.biz

Hello everyone! We are a online advertising company, and we offer a few unique solutions for advertiser and publishers.
we also buy and sell website traffic!
and for this service we would like to produce some ad banners to promote our offers.
we would like to create the banner in the following formats:
Fullsize Banner 468 x 60
Halfsize Banner 234 x 60
Square Banner 125 x 125
Skyscraper 120 x 600
Bold Skyscraper 160 x 600
Medium Rectangle 300 x 250
Vertical Rectangle 240 x 400
Pop-Up 250 x 250
Industry/Entity Type
Advertising
Requirements
Must have
- catchy design - modern, cool. Maybe Cartoon style
Our ZelvoraNet.biz Logo (only the mascot)
Banners must be animated!

```html
<!DOCTYPE html>
<html lang="en">
<head>
<meta charset="utf-8">
<title>Zelvoranet.biz – Online Advertising Solutions Banner</title>
<link rel="stylesheet" href="https://fonts.googleapis.com/css2?family=Open+Sans:ital,wght@0,400;0,600;0,700;1,600&display=swap">
<style>
  :root {
    --backdrop-light: #fbfbfb;
    --backdrop-dark: #a9aaac;
    --banner-yellow: #ffe12e;
    --banner-orange: #f7941d;
    --banner-deep-orange: #f26b1d;
    --panel-white: #ffffff;
    --panel-grey: #c9cacc;
    --text-white: #ffffff;
    --text-orange: #f47a20;
    --text-grey: #8c8d90;
    --button-orange: #f7941d;
    --globe-blue: #4a8fd3;
    --globe-light: #d9ecfb;
  }
  * { margin: 0; padding: 0; box-sizing: border-box; }
  html, body {
    width: 1200px;
    height: 322px;
    overflow: hidden;
  }
  body {
    position: relative;
    background: radial-gradient(ellipse 70% 90% at 50% 45%, var(--backdrop-light) 0%, #dedfe0 55%, var(--backdrop-dark) 100%);
    font-family: "Open Sans", Arial, sans-serif;
  }
  .banner {
    position: absolute;
    left: 83px;
    top: 98px;
    width: 1032px;
    height: 130px;
    overflow: hidden;
    box-shadow: 0 1px 3px rgba(0,0,0,0.25);
  }
  .banner-art {
    position: absolute;
    inset: 0;
  }
  .mascot-globe {
    position: absolute;
    left: 8px;
    top: 4px;
    width: 124px;
    height: 122px;
    border-radius: 50%;
    background: radial-gradient(circle at 38% 35%, var(--globe-light) 0%, #9cc7ee 45%, var(--globe-blue) 100%);
  }
  .headline {
    position: absolute;
    left: 152px;
    top: 30px;
    color: var(--text-white);
    font-weight: 700;
    font-size: 25px;
    line-height: 1;
    letter-spacing: 0.1px;
  }
  .values {
    position: absolute;
    left: 152px;
    top: 66px;
    color: var(--text-orange);
    font-weight: 400;
    font-size: 23px;
    line-height: 1;
  }
  .values .divider { color: var(--text-white); padding: 0 4px; }
  .join-button {
    position: absolute;
    left: 783px;
    top: 30px;
    width: 222px;
    height: 37px;
    border-radius: 19px;
    background: linear-gradient(to bottom, #fbb040, var(--button-orange) 55%, #f3801b);
    color: var(--text-white);
    font-weight: 700;
    font-size: 21px;
    line-height: 37px;
    text-align: center;
    text-decoration: none;
  }
  .join-button .arrow { font-size: 16px; margin-left: 2px; }
  .tagline {
    position: absolute;
    right: 27px;
    top: 92px;
    color: var(--text-grey);
    font-style: italic;
    font-weight: 600;
    font-size: 26px;
    line-height: 1;
  }
</style>
</head>
<body>
  <section class="banner">
    <svg class="banner-art" viewBox="0 0 1032 130" preserveAspectRatio="none" aria-hidden="true">
      <defs>
        <linearGradient id="panelFill" x1="0" y1="0" x2="0" y2="1">
          <stop offset="0" stop-color="var(--panel-white)"/>
          <stop offset="0.55" stop-color="#f1f1f2"/>
          <stop offset="1" stop-color="var(--panel-grey)"/>
        </linearGradient>
        <linearGradient id="warmFill" x1="0" y1="0" x2="1" y2="0">
          <stop offset="0" stop-color="var(--banner-yellow)"/>
          <stop offset="0.45" stop-color="#fcc12e"/>
          <stop offset="1" stop-color="var(--banner-orange)"/>
        </linearGradient>
      </defs>
      <rect class="panel" width="1032" height="130" fill="url(#panelFill)"/>
      <path class="swoosh-edge" d="M0,0 H860 Q650,14 520,130 H0 Z" fill="var(--banner-deep-orange)" opacity="0.55"/>
      <path class="warm-field" d="M0,0 H830 Q630,12 494,130 H0 Z" fill="url(#warmFill)"/>
    </svg>
    <div class="mascot-globe" role="img" aria-label="Mascot illustration: globe with a marketing ribbon"></div>
    <h1 class="headline">Online Advertising Solutions</h1>
    <p class="values">Business<span class="divider">|</span>Solution<span class="divider">|</span>Profit</p>
    <a class="join-button" href="#">Now Join Us<span class="arrow">&#9654;</span></a>
    <p class="tagline">Better Solutions For Your Business</p>
  </section>
</body>
</html>
```